Lower-middle market private equity firm needs its PowerPoint template update/refresh

Brackwell Thorne Equity Partners is a lower-middle market private equity firm focused on acquiring family- and founder-owned businesses in the industrial market. Website is here for more info: https://www.bteqx.com/. We would like to upgrade/update our powerpoint template/slide master we use for marketing materials - uploading a powerpoint version with some of the slide templates we use. We would like to keep it classic and clean with a white background and color on top and enough room for text on the pages. We would prefer to stay within the color palette of the hash tag logo on the cover page (cover page needs an update as well). We are open to suggestions on the font we utilize as well.

```html
<!DOCTYPE html>
<html lang="en">
<head>
<meta charset="utf-8">
<title>Brackwell Thorne Equity Partners — Slide Template Overview</title>
<link href="https://fonts.googleapis.com/css2?family=Archivo:wght@400;600;800;900&family=Inter:ital,wght@0,400;0,600;0,700;1,400&display=swap" rel="stylesheet">
<style>
:root{
  --blue:#2f6ea5;--lblue:#4d95d3;--gold:#b8a833;--green:#3b8c68;--teal:#48a68f;
  --dkgreen:#2d6a4b;--navy:#2a4c7a;--lav:#c6cce4;--beige:#f1eee9;--ink:#333;--grey:#8a8a8a;--page:#e9e9e9;
}
*{margin:0;padding:0;box-sizing:border-box}
html,body{width:1200px;height:2824px;overflow:hidden;background:var(--page)}
body{font-family:"Inter",sans-serif;color:var(--ink)}
.sheet{display:grid;grid-template-columns:repeat(3,337px);grid-auto-rows:252px;gap:24px 18px;padding:46px 0 0 77px}
.slide{position:relative;overflow:hidden;background:#fff;width:337px;height:252px}
.abs{position:absolute}
.fill{position:absolute;inset:0}
svg.fill{width:100%;height:100%}
.logo{font-family:"Archivo",sans-serif;font-weight:800;color:var(--navy);line-height:1;letter-spacing:.02em;display:flex;align-items:center;gap:4px}
.logo i{display:block;background:var(--teal)}
.logo.white{color:#fff}
.logo.white i{background:#fff}
.h-cover{font-family:"Archivo",sans-serif;font-weight:800;color:var(--blue);line-height:1.05}
.tag{font-style:italic;color:#555}
.pills{display:flex;gap:4px}
.pill{font-size:3.6px;color:#fff;padding:2px 6px;border-radius:5px}
.values{display:flex;gap:0;font-size:3.8px;color:#444}
.values span{padding:0 9px;border-left:.6px solid #444}
.values span:first-child{border:0;padding-left:0}
.s-title{position:absolute;left:16px;top:18px;font-family:"Archivo",sans-serif;font-weight:800;font-size:10px;color:var(--blue)}
.s-sub{position:absolute;left:16px;top:31px;font-size:6.6px;color:#444}
.s-rule{position:absolute;left:16px;right:24px;top:42px;height:.6px;background:#bdbdbd}
.mark{position:absolute;right:5px;top:8px;width:11px;height:11px;background:var(--teal)}
.foot{position:absolute;left:16px;right:16px;bottom:4px;font-size:3.4px;color:#666}
.foot .note{margin-bottom:3px;color:#999}
.foot .row{display:flex}
.foot .row span:nth-child(1){width:110px}
.foot .row span:nth-child(2){flex:1}
.kicker{position:absolute;left:16px;top:52px;font-size:6px;font-weight:700;color:var(--gold)}
.body{font-size:5px;line-height:1.4;color:#333}
.body .b{padding-left:8px;position:relative}
.body .b:before{content:"›";position:absolute;left:2px}
.body .s{padding-left:18px;position:relative}
.body .s:before{content:"›";position:absolute;left:12px}
.diag{position:absolute;inset:0;background:var(--beige);clip-path:polygon(55% 0,100% 0,100% 100%,42% 100%)}
.card{position:absolute;background:#fff;box-shadow:0 1px 3px rgba(0,0,0,.18)}
.chip{color:#fff;font-family:"Archivo",sans-serif;font-weight:800;font-size:4.8px;display:flex;align-items:center;justify-content:center;text-align:center}
.bg-blue{background:var(--blue)}.bg-gold{background:var(--gold)}.bg-green{background:var(--green)}
.photo{position:absolute}
.divtitle{font-family:"Archivo",sans-serif;font-weight:800;color:#fff;font-size:12px;line-height:1.1}
.tiny{font-size:4px;line-height:1.35}
table.grid{position:absolute;left:16px;top:62px;width:300px;border-collapse:collapse;font-size:4px}
table.grid th{color:#fff;font-family:"Archivo",sans-serif;font-weight:800;font-size:5px;padding:4px 6px;text-align:left}
table.grid td{padding:6px 6px;border-bottom:.5px solid #ccc}
</style>
</head>
<body>
<main class="sheet">

<!-- 1 Cover A -->
<section class="slide">
  <svg class="fill" viewBox="0 0 337 252" aria-hidden="true">
    <defs><linearGradient id="g1" x1="0" y1="0" x2="1" y2="1"><stop offset="0" stop-color="#7bb36f"/><stop offset=".5" stop-color="#3f9a80"/><stop offset="1" stop-color="#2f8a86"/></linearGradient></defs>
    <rect x="140" width="197" height="252" fill="url(#g1)"/>
    <polygon points="150,252 300,110 300,252" fill="var(--gold)"/>
    <polygon points="0,0 215,0 300,126 215,252 0,252" fill="var(--lav)"/>
    <polygon points="0,0 170,0 262,126 170,252 0,252" fill="#fff"/>
  </svg>
  <div class="logo abs" style="left:26px;top:68px;font-size:11px"><i style="width:12px;height:12px"></i><span>BRACKWELL<br>THORNE</span></div>
  <div class="h-cover abs" style="left:26px;top:118px;font-size:8.5px;color:#333">Realizing the promise in small<br>companies for decades</div>
  <div class="tag abs" style="left:26px;top:144px;font-size:5.5px">Realizing the promise in<br>small companies for decades</div>
  <div class="pills abs" style="left:26px;top:166px"><span class="pill bg-blue">Perseverance</span><span class="pill bg-gold">Ingenuity</span><span class="pill" style="background:var(--lblue)">Transparency</span><span class="pill bg-green">Results</span></div>
</section>

<!-- 2 Cover B -->
<section class="slide" style="background:#fff">
  <div class="abs" style="left:14px;top:14px;right:14px;bottom:14px;background:var(--beige)"></div>
  <div class="abs" style="left:14px;top:14px;right:14px;height:2px;background:linear-gradient(90deg,var(--blue),var(--gold),var(--green))"></div>
  <div class="logo abs" style="left:24px;top:28px;font-size:8px"><i style="width:10px;height:10px"></i><span>BRACKWELL<br>THORNE</span></div>
  <div class="abs" style="left:14px;top:96px;width:240px;height:46px;background:#e6e1da"></div>
  <div class="h-cover abs" style="left:26px;top:104px;font-size:11px">Realizing the promise in small<br>companies for decades</div>
  <div class="abs" style="left:262px;top:88px;width:30px;height:30px;background:var(--teal)"></div>
  <div class="tag abs" style="left:26px;top:168px;font-size:6.5px">Realizing the promise in<br>small companies for decades</div>
  <div class="values abs" style="left:26px;top:195px"><span>Perseverance</span><span>Ingenuity</span><span>Transparency</span><span>Results</span></div>
</section>

<!-- 3 Cover C -->
<section class="slide">
  <svg class="fill" viewBox="0 0 337 252" aria-hidden="true">
    <defs><linearGradient id="g3" x1="0" y1="0" x2="1" y2="1"><stop offset="0" stop-color="#6fae6e"/><stop offset=".55" stop-color="#3f9a80"/><stop offset="1" stop-color="#2f8f88"/></linearGradient></defs>
    <rect width="337" height="252" fill="url(#g3)"/>
    <polygon points="0,0 45,0 160,126 45,252 0,252" fill="var(--lav)"/>
    <polygon points="0,0 15,0 132,126 15,252 0,252" fill="#fff"/>
    <polygon points="0,252 15,252 132,126 150,150 70,252" fill="var(--gold)" opacity=".9"/>
  </svg>
  <div class="logo abs" style="left:12px;top:114px;font-size:8px"><i style="width:9px;height:9px"></i><span>BRACKWELL<br>THORNE</span></div>
  <div class="h-cover abs" style="left:178px;top:90px;font-size:10px;color:#fff">Realizing the promise<br>in small companies<br>for decades</div>
  <div class="tag abs" style="left:178px;top:130px;font-size:5.5px;color:#fff">Realizing the promise in<br>small companies for decades</div>
  <div class="values abs" style="left:178px;top:153px;color:#fff"><span style="border-color:#fff">Perseverance</span><span style="border-color:#fff">Ingenuity</span><span style="border-color:#fff">Transparency</span><span style="border-color:#fff">Results</span></div>
</section>

<!-- 4 Cover D photo -->
<section class="slide" style="background:var(--beige)">
  <div class="abs" style="left:0;top:0;right:0;height:2px;background:linear-gradient(90deg,var(--blue),var(--gold),var(--green))"></div>
  <div class="photo" role="img" aria-label="Engineer in a dark jacket inspecting machinery" style="inset:0;clip-path:polygon(62% 0,100% 0,100% 100%,45% 100%);background:linear-gradient(135deg,#2c3e50,#1a2633 60%,#3b4a57)"></div>
  <div class="logo abs" style="left:16px;top:18px;font-size:8px"><i style="width:10px;height:10px"></i><span>BRACKWELL<br>THORNE</span></div>
  <div class="h-cover abs" style="left:16px;top:86px;font-size:11px">Realizing the promise<br>in small companies<br>for decades</div>
  <div class="abs" style="left:0;top:178px;width:165px;height:50px;background:#e6e1da"></div>
  <div class="tag abs" style="left:16px;top:186px;font-size:5.5px">Realizing the promise in<br>small companies for decades</div>
  <div class="values abs" style="left:16px;top:211px"><span>Perseverance</span><span>Ingenuity</span><span>Transparency</span><span>Results</span></div>
</section>

<!-- 5 Cover E -->
<section class="slide">
  <svg class="fill" viewBox="0 0 337 252" aria-hidden="true">
    <polygon points="0,40 60,126 0,212" fill="var(--green)" opacity=".85"/>
    <polygon points="0,90 25,126 0,162" fill="var(--lav)"/>
    <polygon points="337,80 275,150 337,230" fill="var(--gold)"/>
    <polygon points="337,60 285,126 337,180" fill="var(--lav)"/>
  </svg>
  <div class="logo abs" style="left:110px;top:60px;font-size:11px"><i style="width:12px;height:12px"></i><span>BRACKWELL<br>THORNE</span></div>
  <div class="h-cover abs" style="left:0;right:0;top:112px;text-align:center;font-size:7.5px;color:#333">Realizing the promise in small<br>companies for decades</div>
  <div class="tag abs" style="left:0;right:0;top:134px;text-align:center;font-size:5px">Realizing the promise in<br>small companies for decades</div>
  <div class="pills abs" style="left:92px;top:154px"><span class="pill bg-blue">Perseverance</span><span class="pill bg-gold">Ingenuity</span><span class="pill" style="background:var(--lblue)">Transparency</span><span class="pill bg-green">Results</span></div>
</section>

<!-- 6 Cover F -->
<section class="slide">
  <div class="abs" style="left:14px;top:14px;right:14px;bottom:14px;background:var(--beige)"></div>
  <div class="abs" style="left:14px;top:14px;right:14px;height:2px;background:linear-gradient(90deg,var(--blue),var(--gold),var(--green))"></div>
  <div class="logo abs" style="left:24px;top:28px;font-size:8px"><i style="width:10px;height:10px"></i><span>BRACKWELL<br>THORNE</span></div>
  <div class="abs" style="left:14px;top:96px;width:250px;height:46px;background:#e6e1da"></div>
  <div class="h-cover abs" style="left:26px;top:104px;font-size:11px">Realizing the promise in small<br>companies for decades</div>
  <div class="abs" style="left:270px;top:82px;width:34px;height:34px;background:var(--navy)"></div>
  <div class="tag abs" style="left:26px;top:168px;font-size:6.5px">Realizing the promise in<br>small companies for decades</div>
  <div class="values abs" style="left:26px;top:195px"><span>Perseverance</span><span>Ingenuity</span><span>Transparency</span><span>Results</span></div>
  <div class="abs" style="right:6px;bottom:4px;font-size:3.5px">4</div>
</section>

<!-- 7 Divider teal -->
<section class="slide">
  <div class="photo fill" role="img" aria-label="Robotic arm in an automated factory, tinted teal" style="background:linear-gradient(135deg,#5aa797,#3f8d7e 50%,#2f7a6d)"></div>
  <svg class="fill" viewBox="0 0 337 252" aria-hidden="true">
    <polygon points="0,0 150,0 60,110 0,110" fill="var(--lav)" opacity=".9"/>
    <polygon points="0,0 130,0 45,100 0,100" fill="#fff"/>
    <polygon points="0,0 100,0 70,35" fill="var(--green)" opacity=".7"/>
    <polygon points="0,110 60,110 0,180" fill="var(--gold)" opacity=".6"/>
  </svg>
  <div class="logo abs" style="left:10px;top:60px;font-size:8px"><i style="width:9px;height:9px"></i><span>BRACKWELL<br>THORNE</span></div>
  <div class="divtitle abs" style="left:168px;top:122px;font-size:10px">Divider Title Here</div>
  <div class="abs tiny" style="left:168px;top:138px;color:#fff;font-size:5px">Lorem Ipsum is simply dummy text</div>
</section>

<!-- 8 Divider green -->
<section class="slide">
  <div class="abs" style="left:14px;top:14px;width:192px;height:224px;background:var(--green)"></div>
  <div class="abs" style="left:14px;top:14px;width:192px;height:112px;background:var(--dkgreen)"></div>
  <div class="photo" role="img" aria-label="Automated production plant with digital overlay" style="left:206px;top:14px;right:14px;height:224px;background:linear-gradient(160deg,#5c7f8a,#2d4a55 55%,#6d8a86)"></div>
  <div class="abs" style="left:200px;top:108px;width:14px;height:14px;background:var(--teal)"></div>
  <div class="divtitle abs" style="left:26px;top:92px">Divider Slide<br>Text Here</div>
  <div class="abs tiny" style="left:26px;top:168px;color:#fff;font-size:5px">Lorem Ipsum is simply dummy text</div>
  <div class="foot"><div class="row"><span>BRACKWELL THORNE EQUITY PARTNERS</span><span>CONFIDENTIAL</span><span>BTEQX.com | 8</span></div></div>
</section>

<!-- 9 TOC -->
<section class="slide" style="background:var(--beige)">
  <svg class="fill" viewBox="0 0 337 252" aria-hidden="true">
    <defs><linearGradient id="g9" x1="0" y1="0" x2="1" y2="1"><stop offset="0" stop-color="#6fae6e"/><stop offset="1" stop-color="#2f8f88"/></linearGradient></defs>
    <polygon points="0,0 125,0 0,190" fill="url(#g9)"/>
  </svg>
  <div class="divtitle abs" style="left:14px;top:26px;font-size:11px">Table of<br>Content</div>
  <div class="mark"></div>
  <div class="abs" style="left:132px;top:30px;width:140px;font-size:4.4px">
    <div style="display:flex;align-items:center;gap:6px;height:33px;border-bottom:.5px solid #999"><b style="color:var(--blue);font-size:9px;font-family:Archivo,sans-serif">1</b>Lorem ipsum dolor sit amet</div>
    <div style="display:flex;align-items:center;gap:6px;height:33px;border-bottom:.5px solid #999"><b style="color:var(--blue);font-size:9px;font-family:Archivo,sans-serif">2</b>Consectetur adipiscing elit</div>
    <div style="display:flex;align-items:center;gap:6px;height:33px;border-bottom:.5px solid #999"><b style="color:var(--blue);font-size:9px;font-family:Archivo,sans-serif">3</b>Phasellus malesuada vulputate mauris</div>
    <div style="display:flex;align-items:center;gap:6px;height:33px;border-bottom:.5px solid #999"><b style="color:var(--blue);font-size:9px;font-family:Archivo,sans-serif">4</b>Vitae pretium felis vestibulum vel</div>
    <div style="display:flex;align-items:center;gap:6px;height:33px;border-bottom:.5px solid #999"><b style="color:var(--blue);font-size:9px;font-family:Archivo,sans-serif">5</b>Vestibulum non sagittis orci</div>
    <div style="display:flex;align-items:center;gap:6px;height:33px"><b style="color:var(--blue);font-size:9px;font-family:Archivo,sans-serif">6</b>Fusce finibus elit et felis imperdiet</div>
  </div>
  <div class="foot"><div class="note">Footnote sample: Lorem ipsum dolor sit amet.</div><div class="row"><span>BRACKWELL THORNE EQUITY PARTNERS</span><span>CONFIDENTIAL</span><span>BTEQX.com | 9</span></div></div>
</section>

<!-- 10 One column -->
<section class="slide">
  <div class="s-title">One Column Sample</div><div class="s-sub">Sub Title Goes Here</div><div class="s-rule"></div><div class="mark"></div>
  <div class="kicker">Heading Title Here</div>
  <div class="abs body" style="left:16px;top:62px;width:290px">
    <div class="b">Lorem ipsum dolor sit amet, te ullum corpora delicata duo. Rebum insolens pri eu. No alia tota modus qui.</div><div class="s">Sint brute at usu. Duo iisque appareat adversarium at.</div>
    <div class="b" style="margin-top:3px">Lorem ipsum dolor sit amet, te ullum corpora delicata duo. Rebum insolens pri eu. No alia tota modus qui.</div><div class="s">Sint brute at usu. Duo iisque appareat adversarium at.</div>
    <div class="b" style="margin-top:3px">Lorem ipsum dolor sit amet, te ullum corpora delicata duo. Rebum insolens pri eu. No alia tota modus qui.</div><div class="s">Sint brute at usu. Duo iisque appareat adversarium at.</div>
    <div class="b" style="margin-top:3px">Lorem ipsum dolor sit amet, te ullum corpora delicata duo. Rebum insolens pri eu. No alia tota modus qui.</div>
  </div>
  <div class="foot"><div class="note">Footnote sample: Lorem ipsum dolor sit amet.</div><div class="row"><span>BRACKWELL THORNE EQUITY PARTNERS</span><span>CONFIDENTIAL</span><span>BTEQX.com | 10</span></div></div>
</section>

<!-- 11 Three horizontal -->
<section class="slide">
  <div class="s-title">Three Horizontal Sample</div><div class="s-sub">Sub Title Goes Here</div><div class="s-rule"></div><div class="mark"></div>
  <div class="kicker">Heading Title Here</div>
  <div class="card" style="left:16px;top:66px;width:300px;height:30px"></div>
  <div class="chip bg-blue abs" style="left:16px;top:68px;width:66px;height:26px">Text Title<br>Content 1</div>
  <div class="abs body" style="left:92px;top:73px;width:210px;font-size:4.4px">Lorem ipsum dolor sit amet, te ullum corpora delicata duo. Rebum insolens pri eu. No alia tota modus qui.</div>
  <div class="card" style="left:16px;top:103px;width:300px;height:30px"></div>
  <div class="chip bg-gold abs" style="left:16px;top:105px;width:66px;height:26px">Text Title<br>Content 2</div>
  <div class="abs body" style="left:92px;top:110px;width:210px;font-size:4.4px">Lorem ipsum dolor sit amet, te ullum corpora delicata duo. Rebum insolens pri eu. No alia tota modus qui.</div>
  <div class="card" style="left:16px;top:140px;width:300px;height:30px"></div>
  <div class="chip bg-blue abs" style="left:16px;top:142px;width:66px;height:26px">Text Title<br>Content 3</div>
  <div class="abs body" style="left:92px;top:147px;width:210px;font-size:4.4px">Lorem ipsum dolor sit amet, te ullum corpora delicata duo. Rebum insolens pri eu. No alia tota modus qui.</div>
  <div class="card" style="left:16px;top:177px;width:300px;height:30px"></div>
  <div class="chip bg-gold abs" style="left:16px;top:179px;width:66px;height:26px">Text Title<br>Content 4</div>
  <div class="abs body" style="left:92px;top:184px;width:210px;font-size:4.4px">Lorem ipsum dolor sit amet, te ullum corpora delicata duo. Rebum insolens pri eu. No alia tota modus qui.</div>
  <div class="foot"><div class="note">Footnote sample: Lorem ipsum dolor sit amet.</div><div class="row"><span>BRACKWELL THORNE EQUITY PARTNERS</span><span>CONFIDENTIAL</span><span>BTEQX.com | 11</span></div></div>
</section>

<!-- 12 Three image cards -->
<section class="slide">
  <div class="s-title">Presentation Title here</div><div class="s-sub">Sub Title Goes Here</div><div class="s-rule"></div><div class="mark"></div>
  <div class="card" style="left:16px;top:52px;width:96px;height:170px"></div>
  <div class="photo" role="img" aria-label="Group photo of the team" style="left:16px;top:52px;width:96px;height:60px;background:linear-gradient(180deg,#b9c4cf,#4b5a6a)"></div>
  <div class="chip bg-blue abs" style="left:16px;top:112px;width:96px;height:12px;justify-content:flex-start;padding-left:6px">Heading 1</div>
  <div class="abs body" style="left:20px;top:128px;width:86px;font-size:3.8px"><div class="b">Insert Your Heading text Goes Here</div><div class="b">Lorem ipsum dolor sit amet, consectetur</div><div class="b">Phasellus malesuada vulputate mauris.</div><div class="b">vitae pretium felis vestibulum vel.</div></div>
  <div class="card" style="left:120px;top:52px;width:96px;height:170px"></div>
  <div class="photo" role="img" aria-label="Industrial machinery close-up in warm light" style="left:120px;top:52px;width:96px;height:60px;background:linear-gradient(160deg,#e9c59a,#9a6a3c 60%,#5a4030)"></div>
  <div class="chip bg-gold abs" style="left:120px;top:112px;width:96px;height:12px;justify-content:flex-start;padding-left:6px">Heading 2</div>
  <div class="abs body" style="left:124px;top:128px;width:86px;font-size:3.8px"><div class="b">Insert Your Heading text Goes Here</div><div class="b">Lorem ipsum dolor sit amet, consectetur</div><div class="b">Phasellus malesuada vulputate mauris.</div><div class="b">vitae pretium felis vestibulum vel.</div></div>
  <div class="card" style="left:224px;top:52px;width:96px;height:170px"></div>
  <div class="photo" role="img" aria-label="Team at a trade show booth" style="left:224px;top:52px;width:96px;height:60px;background:linear-gradient(180deg,#c9a0a0,#3a3030)"></div>
  <div class="chip bg-blue abs" style="left:224px;top:112px;width:96px;height:12px;justify-content:flex-start;padding-left:6px">Heading 3</div>
  <div class="abs body" style="left:228px;top:128px;width:86px;font-size:3.8px"><div class="b">Insert Your Heading text Goes Here</div><div class="b">Lorem ipsum dolor sit amet, consectetur</div><div class="b">Phasellus malesuada vulputate mauris.</div><div class="b">vitae pretium felis vestibulum vel.</div></div>
  <div class="foot"><div class="note">Footnote sample: Lorem ipsum dolor sit amet.</div><div class="row"><span>BRACKWELL THORNE EQUITY PARTNERS</span><span>CONFIDENTIAL</span><span>BTEQX.com | 12</span></div></div>
</section>

<!-- 13 Six points -->
<section class="slide">
  <div class="s-title">6 Poin Content</div><div class="s-sub">Sub Title Goes Here</div><div class="s-rule"></div><div class="mark"></div>
  <div class="abs" style="left:16px;top:56px;width:300px;display:grid;grid-template-columns:repeat(3,96px);grid-auto-rows:80px;gap:8px 6px">
    <div style="background:#fff;box-shadow:0 1px 3px rgba(0,0,0,.18)"><div class="chip bg-blue" style="height:22px;justify-content:flex-start;padding-left:6px">Heading Text 1</div><p class="body" style="font-size:3.8px;padding:6px">Lorem Ipsum has been the industry's standard dummy text ever since the 1500s, when an unknown printer took a galley of type to make a type specimen book.</p></div>
    <div style="background:#fff;box-shadow:0 1px 3px rgba(0,0,0,.18)"><div class="chip bg-gold" style="height:22px;justify-content:flex-start;padding-left:6px">Heading Text 2</div><p class="body" style="font-size:3.8px;padding:6px">Lorem Ipsum has been the industry's standard dummy text ever since the 1500s, when an unknown printer took a galley of type to make a type specimen book.</p></div>
    <div style="background:#fff;box-shadow:0 1px 3px rgba(0,0,0,.18)"><div class="chip bg-blue" style="height:22px;justify-content:flex-start;padding-left:6px">Heading Text 3</div><p class="body" style="font-size:3.8px;padding:6px">Lorem Ipsum has been the industry's standard dummy text ever since the 1500s, when an unknown printer took a galley of type to make a type specimen book.</p></div>
    <div style="background:#fff;box-shadow:0 1px 3px rgba(0,0,0,.18)"><div class="chip bg-gold" style="height:22px;justify-content:flex-start;padding-left:6px">Heading Text 4</div><p class="body" style="font-size:3.8px;padding:6px">Lorem Ipsum has been the industry's standard dummy text ever since the 1500s, when an unknown printer took a galley of type to make a type specimen book.</p></div>
    <div style="background:#fff;box-shadow:0 1px 3px rgba(0,0,0,.18)"><div class="chip bg-blue" style="height:22px;justify-content:flex-start;padding-left:6px">Heading Text 5</div><p class="body" style="font-size:3.8px;padding:6px">Lorem Ipsum has been the industry's standard dummy text ever since the 1500s, when an unknown printer took a galley of type to make a type specimen book.</p></div>
    <div style="background:#fff;box-shadow:0 1px 3px rgba(0,0,0,.18)"><div class="chip bg-gold" style="height:22px;justify-content:flex-start;padding-left:6px">Heading Text 6</div><p class="body" style="font-size:3.8px;padding:6px">Lorem Ipsum has been the industry's standard dummy text ever since the 1500s, when an unknown printer took a galley of type to make a type specimen book.</p></div>
  </div>
  <div class="foot"><div class="note">Footnote sample: Lorem ipsum dolor sit amet.</div><div class="row"><span>BRACKWELL THORNE EQUITY PARTNERS</span><span>CONFIDENTIAL</span><span>BTEQX.com | 13</span></div></div>
</section>

<!-- 14 Bar chart -->
<section class="slide">
  <div class="diag"></div>
  <div class="s-title">Bar Chart Sample</div><div class="s-sub">Sub Title Goes Here</div><div class="s-rule" style="right:170px"></div><div class="mark"></div>
  <div class="kicker">Heading Title Here</div>
  <div class="abs body" style="left:16px;top:62px;width:140px">
    <div class="b">Lorem ipsum dolor sit amet, te ullum corpora delicata duo. Rebum insolens pri eu. No alia tota modus qui.</div><div class="s">Sint brute at usu. Duo iisque appareat adversarium at.</div>
    <div class="b" style="margin-top:3px">Lorem ipsum dolor sit amet, te ullum corpora delicata duo. Rebum insolens pri eu. No alia tota modus qui.</div><div class="s">Sint brute at usu. Duo iisque appareat adversarium at.</div>
  </div>
  <svg class="abs" style="left:180px;top:70px" width="130" height="120" viewBox="0 0 130 120" font-family="Inter,sans-serif">
    <text x="65" y="6" font-size="6" font-weight="700" text-anchor="middle" fill="#222">Heading Here</text>
    <g font-size="4" fill="#444"><text x="0" y="92">0</text><text x="0" y="80">1</text><text x="0" y="68">2</text><text x="0" y="56">3</text><text x="0" y="44">4</text><text x="0" y="32">5</text><text x="0" y="20">6</text></g>
    <g fill="var(--blue)"><rect x="12" y="42" width="4" height="48"/><rect x="40" y="60" width="4" height="30"/><rect x="68" y="54" width="4" height="36"/><rect x="96" y="36" width="4" height="54"/></g>
    <g fill="var(--gold)"><rect x="17" y="60" width="4" height="30"/><rect x="45" y="36" width="4" height="54"/><rect x="73" y="66" width="4" height="24"/><rect x="101" y="60" width="4" height="30"/></g>
    <g fill="var(--lblue)"><rect x="22" y="66" width="4" height="24"/><rect x="50" y="66" width="4" height="24"/><rect x="78" y="54" width="4" height="36"/><rect x="106" y="30" width="4" height="60"/></g>
    <g font-size="4" fill="#444" text-anchor="middle"><text x="19" y="98">Category 1</text><text x="47" y="98">Category 2</text><text x="75" y="98">Category 3</text><text x="103" y="98">Category 4</text></g>
    <g font-size="4" fill="#444"><rect x="24" y="104" width="3" height="3" fill="var(--blue)"/><text x="28" y="107">Series 1</text><rect x="50" y="104" width="3" height="3" fill="var(--gold)"/><text x="54" y="107">Series 2</text><rect x="76" y="104" width="3" height="3" fill="var(--lblue)"/><text x="80" y="107">Series 3</text></g>
  </svg>
  <div class="foot"><div class="note">Footnote sample: Lorem ipsum dolor sit amet.</div><div class="row"><span>BRACKWELL THORNE EQUITY PARTNERS</span><span>CONFIDENTIAL</span><span>BTEQX.com | 14</span></div></div>
</section>

<!-- 15 Line chart -->
<section class="slide">
  <div class="diag"></div>
  <div class="s-title">Line Chart Sample</div><div class="s-sub">Sub Title Goes Here</div><div class="s-rule" style="right:170px"></div><div class="mark"></div>
  <div class="kicker">Heading Title Here</div>
  <div class="abs body" style="left:16px;top:62px;width:140px">
    <div class="b">Lorem ipsum dolor sit amet, te ullum corpora delicata duo. Rebum insolens pri eu. No alia tota modus qui.</div><div class="s">Sint brute at usu. Duo iisque appareat adversarium at.</div>
    <div class="b" style="margin-top:3px">Lorem ipsum dolor sit amet, te ullum corpora delicata duo. Rebum insolens pri eu. No alia tota modus qui.</div><div class="s">Sint brute at usu. Duo iisque appareat adversarium at.</div>
  </div>
  <svg class="abs" style="left:180px;top:70px" width="130" height="120" viewBox="0 0 130 120" font-family="Inter,sans-serif">
    <text x="65" y="6" font-size="6" font-weight="700" text-anchor="middle" fill="#222">Heading Here</text>
    <g font-size="4" fill="#444"><text x="0" y="92">0</text><text x="0" y="80">1</text><text x="0" y="68">2</text><text x="0" y="56">3</text><text x="0" y="44">4</text><text x="0" y="32">5</text><text x="0" y="20">6</text></g>
    <polyline points="18,58 46,70 74,62 102,40" fill="none" stroke="var(--blue)" stroke-width="1"/>
    <polyline points="18,72 46,46 74,72 102,62" fill="none" stroke="var(--gold)" stroke-width="1"/>
    <polyline points="18,78 46,72 74,58 102,44" fill="none" stroke="var(--lblue)" stroke-width="1"/>
    <g font-size="4" fill="#444" text-anchor="middle"><text x="18" y="98">Category 1</text><text x="46" y="98">Category 2</text><text x="74" y="98">Category 3</text><text x="102" y="98">Category 4</text></g>
    <g font-size="4" fill="#444"><line x1="22" y1="105" x2="28" y2="105" stroke="var(--blue)"/><text x="29" y="107">Series 1</text><line x1="48" y1="105" x2="54" y2="105" stroke="var(--gold)"/><text x="55" y="107">Series 2</text><line x1="74" y1="105" x2="80" y2="105" stroke="var(--lblue)"/><text x="81" y="107">Series 3</text></g>
  </svg>
  <div class="foot"><div class="note">Footnote sample: Lorem ipsum dolor sit amet.</div><div class="row"><span>BRACKWELL THORNE EQUITY PARTNERS</span><span>CONFIDENTIAL</span><span>BTEQX.com | 15</span></div></div>
</section>

<!-- 16 Pie chart -->
<section class="slide">
  <div class="diag"></div>
  <div class="s-title">Pie Chart Sample</div><div class="s-sub">Sub Title Goes Here</div><div class="s-rule" style="right:170px"></div><div class="mark"></div>
  <div class="kicker">Heading Title Here</div>
  <div class="abs body" style="left:16px;top:62px;width:140px">
    <div class="b">Lorem ipsum dolor sit amet, te ullum corpora delicata duo. Rebum insolens pri eu. No alia tota modus qui.</div><div class="s">Sint brute at usu. Duo iisque appareat adversarium at.</div>
    <div class="b" style="margin-top:3px">Lorem ipsum dolor sit amet, te ullum corpora delicata duo. Rebum insolens pri eu. No alia tota modus qui.</div><div class="s">Sint brute at usu. Duo iisque appareat adversarium at.</div>
  </div>
  <svg class="abs" style="left:180px;top:66px" width="130" height="120" viewBox="0 0 130 120" font-family="Inter,sans-serif">
    <text x="65" y="6" font-size="6" font-weight="700" text-anchor="middle" fill="#222">Heading Here</text>
    <g transform="translate(65,54) rotate(-90)">
      <circle r="12.5" fill="none" stroke="var(--blue)" stroke-width="25" stroke-dasharray="23.6 78.6"/>
      <circle r="12.5" fill="none" stroke="var(--gold)" stroke-width="25" stroke-dasharray="15.7 78.6" stroke-dashoffset="-23.6"/>
      <circle r="12.5" fill="none" stroke="var(--lblue)" stroke-width="25" stroke-dasharray="19.6 78.6" stroke-dashoffset="-39.3"/>
      <circle r="12.5" fill="none" stroke="var(--green)" stroke-width="25" stroke-dasharray="19.7 78.6" stroke-dashoffset="-58.9"/>
    </g>
    <g font-size="6" font-weight="700" fill="#333"><text x="96" y="34">4.3%</text><text x="96" y="84">2.5%</text><text x="22" y="90">3.5%</text><text x="14" y="40">4.5%</text></g>
    <g font-size="3.6" fill="#444"><rect x="14" y="103" width="3" height="3" fill="var(--blue)"/><text x="18" y="106">Category 1</text><rect x="40" y="103" width="3" height="3" fill="var(--gold)"/><text x="44" y="106">Category 2</text><rect x="66" y="103" width="3" height="3" fill="var(--lblue)"/><text x="70" y="106">Category 3</text><rect x="92" y="103" width="3" height="3" fill="var(--green)"/><text x="96" y="106">Category 4</text></g>
  </svg>
  <div class="foot"><div class="note">Footnote sample: Lorem ipsum dolor sit amet.</div><div class="row"><span>BRACKWELL THORNE EQUITY PARTNERS</span><span>CONFIDENTIAL</span><span>BTEQX.com | 16</span></div></div>
</section>

<!-- 17 Donut chart -->
<section class="slide">
  <div class="diag"></div>
  <div class="s-title">Chart Sample</div><div class="s-sub">Sub Title Goes Here</div><div class="s-rule" style="right:170px"></div><div class="mark"></div>
  <div class="kicker">Heading Title Here</div>
  <div class="abs body" style="left:16px;top:62px;width:140px">
    <div class="b">Lorem ipsum dolor sit amet, te ullum corpora delicata duo. Rebum insolens pri eu. No alia tota modus qui.</div><div class="s">Sint brute at usu. Duo iisque appareat adversarium at.</div>
    <div class="b" style="margin-top:3px">Lorem ipsum dolor sit amet, te ullum corpora delicata duo. Rebum insolens pri eu. No alia tota modus qui.</div><div class="s">Sint brute at usu. Duo iisque appareat adversarium at.</div>
  </div>
  <svg class="abs" style="left:178px;top:80px" width="140" height="100" viewBox="0 0 140 100" font-family="Inter,sans-serif">
    <circle cx="30" cy="30" r="20" fill="#fff" stroke="#e4e4e4" stroke-width="6"/>
    <circle cx="30" cy="30" r="20" fill="none" stroke="var(--blue)" stroke-width="6" stroke-dasharray="100.5 125.7" transform="rotate(-90 30 30)"/>
    <text x="30" y="33" font-size="9" font-weight="700" text-anchor="middle" fill="var(--blue)">80%</text>
    <circle cx="98" cy="30" r="20" fill="#fff" stroke="#e4e4e4" stroke-width="6"/>
    <circle cx="98" cy="30" r="20" fill="none" stroke="var(--gold)" stroke-width="6" stroke-dasharray="75.4 125.7" transform="rotate(-90 98 30)"/>
    <text x="98" y="33" font-size="9" font-weight="700" text-anchor="middle" fill="var(--gold)">60%</text>
    <g text-anchor="middle" fill="#333"><text x="30" y="63" font-size="5" font-weight="700">Data 1</text><text x="30" y="69" font-size="3.8">Lorem ipsum</text><text x="30" y="74" font-size="3.8">dolor sit amet</text>
    <text x="98" y="63" font-size="5" font-weight="700">Data 2</text><text x="98" y="69" font-size="3.8">Lorem ipsum</text><text x="98" y="74" font-size="3.8">dolor sit amet</text></g>
  </svg>
  <div class="foot"><div class="note">Footnote sample: Lorem ipsum dolor sit amet.</div><div class="row"><span>BRACKWELL THORNE EQUITY PARTNERS</span><span>CONFIDENTIAL</span><span>BTEQX.com | 17</span></div></div>
</section>

<!-- 18 Content with image -->
<section class="slide">
  <div class="photo" role="img" aria-label="Two men shaking hands on a factory floor" style="inset:0;clip-path:polygon(52% 0,100% 0,100% 100%,40% 100%);background:linear-gradient(160deg,#c9ccd0,#8c949b 50%,#5a6168)"></div>
  <div class="s-title">Content with Image Sample</div><div class="s-sub">Sub Title Goes Here</div><div class="s-rule" style="right:170px"></div>
  <div class="kicker">Heading Title Here</div>
  <div class="abs body" style="left:16px;top:62px;width:140px">
    <div class="b">Lorem ipsum dolor sit amet, te ullum corpora delicata duo. Rebum insolens pri eu. No alia tota modus qui.</div><div class="s">Sint brute at usu. Duo iisque appareat adversarium at.</div>
    <div class="b" style="margin-top:3px">Lorem ipsum dolor sit amet, te ullum corpora delicata duo. Rebum insolens pri eu. No alia tota modus qui.</div><div class="s">Sint brute at usu. Duo iisque appareat adversarium at.</div>
  </div>
  <div class="foot"><div class="note">Footnote sample: Lorem ipsum dolor sit amet.</div><div class="row"><span>BRACKWELL THORNE EQUITY PARTNERS</span><span>CONFIDENTIAL</span><span>BTEQX.com | 18</span></div></div>
</section>

<!-- 19 Divider forest -->
<section class="slide">
  <div class="photo fill" role="img" aria-label="Misty forest tinted green" style="background:linear-gradient(135deg,#6aa895,#3d8a74 55%,#2d6e5d)"></div>
  <svg class="fill" viewBox="0 0 337 252" aria-hidden="true">
    <polygon points="0,0 185,0 95,110 0,110" fill="var(--lav)" opacity=".9"/>
    <polygon points="0,0 160,0 80,95 0,95" fill="#fff"/>
    <polygon points="0,130 120,130 0,252" fill="var(--gold)" opacity=".95"/>
  </svg>
  <div class="logo abs" style="left:12px;top:52px;font-size:9px"><i style="width:10px;height:10px"></i><span>BRACKWELL<br>THORNE</span></div>
  <div class="divtitle abs" style="left:168px;top:126px;font-size:10px">Divider Title Here</div>
  <div class="abs tiny" style="left:168px;top:142px;color:#fff;font-size:5px">Lorem Ipsum is simply dummy text</div>
</section>

<!-- 20 Divider blue -->
<section class="slide">
  <div class="abs" style="left:14px;top:14px;width:192px;height:224px;background:var(--blue)"></div>
  <div class="abs" style="left:14px;top:14px;width:192px;height:112px;background:#2a5f8e"></div>
  <div class="photo" role="img" aria-label="Hand holding a glowing light bulb with technology icons" style="left:206px;top:14px;right:14px;height:224px;background:linear-gradient(150deg,#2c4e70,#1a2f48 50%,#d38a3c)"></div>
  <div class="abs" style="left:200px;top:108px;width:14px;height:14px;background:var(--teal)"></div>
  <div class="divtitle abs" style="left:26px;top:92px">Divider Slide<br>Text Here</div>
  <div class="abs tiny" style="left:26px;top:168px;color:#fff;font-size:5px">Lorem Ipsum is simply dummy text</div>
  <div class="foot"><div class="row"><span>BRACKWELL THORNE EQUITY PARTNERS</span><span>CONFIDENTIAL</span><span>BTEQX.com | 20</span></div></div>
</section>

<!-- 21 Graphic process -->
<section class="slide">
  <div class="s-title">Graphic Process Sample</div><div class="s-sub">Sub Title Goes Here</div><div class="s-rule"></div><div class="mark"></div>
  <svg class="abs" style="left:20px;top:70px" width="120" height="120" viewBox="0 0 120 120" font-family="Inter,sans-serif">
    <g transform="translate(60,60) rotate(-90)" fill="none" stroke-width="20">
      <circle r="38" stroke="var(--blue)" stroke-dasharray="36 238.8"/>
      <circle r="38" stroke="var(--gold)" stroke-dasharray="36 238.8" stroke-dashoffset="-39.8"/>
      <circle r="38" stroke="var(--blue)" stroke-dasharray="36 238.8" stroke-dashoffset="-79.6"/>
      <circle r="38" stroke="var(--gold)" stroke-dasharray="36 238.8" stroke-dashoffset="-119.4"/>
      <circle r="38" stroke="var(--blue)" stroke-dasharray="36 238.8" stroke-dashoffset="-159.2"/>
      <circle r="38" stroke="var(--gold)" stroke-dasharray="36 238.8" stroke-dashoffset="-199"/>
    </g>
    <g fill="#fff" stroke="var(--blue)" stroke-width=".6" font-size="4" font-weight="700">
      <circle cx="74" cy="20" r="4"/><circle cx="102" cy="60" r="4"/><circle cx="80" cy="96" r="4"/><circle cx="40" cy="96" r="4"/><circle cx="18" cy="60" r="4"/><circle cx="40" cy="22" r="4"/>
    </g>
    <g font-size="4" font-weight="700" fill="var(--blue)" text-anchor="middle"><text x="74" y="21.5">1</text><text x="102" y="61.5">2</text><text x="80" y="97.5">3</text><text x="40" y="97.5">4</text><text x="18" y="61.5">5</text><text x="40" y="23.5">6</text></g>
  </svg>
  <div class="abs" style="left:162px;top:74px;width:150px;font-size:3.8px;line-height:1.35">
    <div style="display:flex;gap:6px;height:23px"><b style="color:var(--blue);font-size:9px;font-family:Archivo,sans-serif">1</b><span>Lorem ipsum dolor sit amet, te ullum corpora delicata duo. Rebum insolens pri eu. No alia tota modus qui.</span></div>
    <div style="display:flex;gap:6px;height:23px"><b style="color:var(--blue);font-size:9px;font-family:Archivo,sans-serif">2</b><span>Lorem ipsum dolor sit amet, te ullum corpora delicata duo. Rebum insolens pri eu. No alia tota modus qui.</span></div>
    <div style="display:flex;gap:6px;height:23px"><b style="color:var(--blue);font-size:9px;font-family:Archivo,sans-serif">3</b><span>Lorem ipsum dolor sit amet, te ullum corpora delicata duo. Rebum insolens pri eu. No alia tota modus qui.</span></div>
    <div style="display:flex;gap:6px;height:23px"><b style="color:var(--blue);font-size:9px;font-family:Archivo,sans-serif">4</b><span>Lorem ipsum dolor sit amet, te ullum corpora delicata duo. Rebum insolens pri eu. No alia tota modus qui.</span></div>
    <div style="display:flex;gap:6px;height:23px"><b style="color:var(--blue);font-size:9px;font-family:Archivo,sans-serif">5</b><span>Lorem ipsum dolor sit amet, te ullum corpora delicata duo. Rebum insolens pri eu. No alia tota modus qui.</span></div>
    <div style="display:flex;gap:6px;height:23px"><b style="color:var(--blue);font-size:9px;font-family:Archivo,sans-serif">6</b><span>Lorem ipsum dolor sit amet, te ullum corpora delicata duo. Rebum insolens pri eu. No alia tota modus qui.</span></div>
  </div>
  <div class="foot"><div class="note">Footnote sample: Lorem ipsum dolor sit amet.</div><div class="row"><span>BRACKWELL THORNE EQUITY PARTNERS</span><span>CONFIDENTIAL</span><span>BTEQX.com | 21</span></div></div>
</section>

<!-- 22 Pyramid -->
<section class="slide">
  <div class="s-title">Presentation Title Here</div><div class="s-sub">Sub Title Goes Here</div><div class="s-rule"></div><div class="mark"></div>
  <svg class="abs" style="left:30px;top:70px" width="140" height="130" viewBox="0 0 140 130" aria-hidden="true">
    <polygon points="70,8 88,36 52,36" fill="var(--navy)"/>
    <polygon points="48,44 92,44 108,72 32,72" fill="var(--gold)"/>
    <polygon points="28,80 112,80 132,116 8,116" fill="var(--lblue)"/>
    <line x1="92" y1="40" x2="108" y2="24" stroke="var(--navy)" stroke-width="1"/>
    <line x1="108" y1="72" x2="124" y2="60" stroke="var(--gold)" stroke-width="1"/>
  </svg>
  <div class="abs" style="left:146px;top:76px;width:160px">
    <div style="font-family:Archivo,sans-serif;font-weight:800;font-size:7px;color:var(--navy)">High</div>
    <div class="tiny">Lorem ipsum dolor sit amet, te ullum corpora delicata duo. Rebum insolens pri eu. No alia tota modus qui.</div>
  </div>
  <div class="abs" style="left:160px;top:114px;width:150px">
    <div style="font-family:Archivo,sans-serif;font-weight:800;font-size:7px;color:var(--gold)">Middle</div>
    <div class="tiny">Lorem ipsum dolor sit amet, te ullum corpora delicata duo. Rebum insolens pri eu. No alia tota modus qui.</div>
  </div>
  <div class="abs" style="left:170px;top:156px;width:140px">
    <div style="font-family:Archivo,sans-serif;font-weight:800;font-size:7px;color:var(--lblue)">Low</div>
    <div class="tiny">Lorem ipsum dolor sit amet, te ullum corpora delicata duo. Rebum insolens pri eu. No alia tota modus qui.</div>
  </div>
  <div class="foot"><div class="note">Footnote sample: Lorem ipsum dolor sit amet.</div><div class="row"><span>BRACKWELL THORNE EQUITY PARTNERS</span><span>CONFIDENTIAL</span><span>BTEQX.com | 22</span></div></div>
</section>

<!-- 23 Text + boxes + quote -->
<section class="slide">
  <div class="s-title">Presentation Title Here</div><div class="s-sub">Sub Title Goes Here</div><div class="s-rule"></div><div class="mark"></div>
  <div class="abs body" style="left:16px;top:58px;width:104px;font-size:4.6px">
    <div class="b">Lorem ipsum dolor sit amet, consectetur adipiscing elit. Phasellus malesuada vulputate mauris, vitae pretium felis vestibulum vel. Vestibulum non sagittis orci. Fusce finibus elit et felis imperdiet</div>
    <div class="b" style="margin-top:3px">Lorem ipsum dolor sit amet, consectetur adipiscing elit. Phasellus malesuada vulputate mauris, vitae pretium felis vestibulum vel. Vestibulum non sagittis orci. Fusce finibus elit et felis imperdiet</div>
  </div>
  <div class="abs bg-blue" style="left:128px;top:58px;width:88px;height:92px;color:#fff;padding:26px 6px 6px;font-size:4px;line-height:1.35">Lorem ipsum dolor sit amet, consectetur adipiscing elit. Phasellus malesuada vulputate mauris, vitae pretium felis vestibulum vel. Vestibulum non sagittis orci. Fusce finibus elit et felis imperdiet</div>
  <div class="abs bg-gold" style="left:222px;top:58px;width:88px;height:92px;color:#fff;padding:26px 6px 6px;font-size:4px;line-height:1.35">Lorem ipsum dolor sit amet, consectetur adipiscing elit. Phasellus malesuada vulputate mauris, vitae pretium felis vestibulum vel. Vestibulum non sagittis orci. Fusce finibus elit et felis imperdiet</div>
  <div class="abs" style="left:136px;top:64px;width:12px;height:12px;border:.8px solid #fff;border-radius:2px"></div>
  <div class="abs" style="left:230px;top:64px;width:12px;height:12px;border:.8px solid #fff;border-radius:2px"></div>
  <div class="abs" style="left:128px;top:156px;width:182px;height:40px;background:var(--lblue);color:#fff;padding:6px 8px;font-size:4px;line-height:1.35"><b style="font-size:9px;font-family:Archivo,sans-serif;line-height:0;vertical-align:-3px">“</b> Lorem ipsum dolor sit amet, consectetur adipiscing elit. Phasellus malesuada vulputate mauris, vitae pretium felis vestibulum vel.<div style="text-align:right;margin-top:4px">- Lorem Ipsum</div></div>
  <div class="foot"><div class="note">Footnote sample: Lorem ipsum dolor sit amet.</div><div class="row"><span>BRACKWELL THORNE EQUITY PARTNERS</span><span>CONFIDENTIAL</span><span>BTEQX.com | 23</span></div></div>
</section>

<!-- 24 About us -->
<section class="slide">
  <div class="s-title">About Us</div><div class="s-sub">Sub Title Goes Here</div><div class="s-rule"></div><div class="mark"></div>
  <div class="abs" style="left:16px;top:56px;width:304px;display:grid;grid-template-columns:repeat(4,70px);gap:8px">
    <div style="height:138px;background:#fff;box-shadow:0 1px 3px rgba(0,0,0,.18)"><div class="chip bg-blue" style="height:30px;justify-content:flex-start;padding-left:22px;text-align:left">Heading<br>Text 1</div><p style="font-size:3.7px;line-height:1.35;padding:6px">Lorem ipsum dolor sit amet, consectetur adipiscing elit. Phasellus malesuada vulputate mauris, vitae pretium felis vestibulum vel. Vestibulum non sagittis orci. Fusce finibus elit et felis imperdiet</p></div>
    <div style="height:138px;background:#fff;box-shadow:0 1px 3px rgba(0,0,0,.18)"><div class="chip bg-gold" style="height:30px;justify-content:flex-start;padding-left:22px;text-align:left">Heading<br>Text 2</div><p style="font-size:3.7px;line-height:1.35;padding:6px">Lorem ipsum dolor sit amet, consectetur adipiscing elit. Phasellus malesuada vulputate mauris, vitae pretium felis vestibulum vel. Vestibulum non sagittis orci. Fusce finibus elit et felis imperdiet</p></div>
    <div style="height:138px;background:#fff;box-shadow:0 1px 3px rgba(0,0,0,.18)"><div class="chip bg-blue" style="height:30px;justify-content:flex-start;padding-left:22px;text-align:left">Heading<br>Text 3</div><p style="font-size:3.7px;line-height:1.35;padding:6px">Lorem ipsum dolor sit amet, consectetur adipiscing elit. Phasellus malesuada vulputate mauris, vitae pretium felis vestibulum vel. Vestibulum non sagittis orci. Fusce finibus elit et felis imperdiet</p></div>
    <div style="height:138px;background:#fff;box-shadow:0 1px 3px rgba(0,0,0,.18)"><div class="chip bg-gold" style="height:30px;justify-content:flex-start;padding-left:22px;text-align:left">Heading<br>Text 4</div><p style="font-size:3.7px;line-height:1.35;padding:6px">Lorem ipsum dolor sit amet, consectetur adipiscing elit. Phasellus malesuada vulputate mauris, vitae pretium felis vestibulum vel. Vestibulum non sagittis orci. Fusce finibus elit et felis imperdiet</p></div>
  </div>
  <div class="abs" style="left:16px;top:202px;width:302px;height:12px;background:var(--lblue);color:#fff;font-size:5px;display:flex;align-items:center;justify-content:center">Lorem ipsum dolor sit amet, consectetur adipiscing elit.</div>
  <div class="foot"><div class="note">Footnote sample: Lorem ipsum dolor sit amet.</div><div class="row"><span>BRACKWELL THORNE EQUITY PARTNERS</span><span>CONFIDENTIAL</span><span>BTEQX.com | 24</span></div></div>
</section>

<!-- 25 Table -->
<section class="slide">
  <div class="s-title">Table Sample</div><div class="s-sub">Sub Title Goes Here</div><div class="s-rule"></div><div class="mark"></div>
  <table class="grid">
    <thead><tr><th style="background:var(--navy)">Heading 1</th><th class="bg-gold">Heading 2</th><th style="background:var(--lblue)">Heading 3</th><th class="bg-green">Heading 4</th></tr></thead>
    <tbody>
      <tr><td>Lorem ipsum dolor sit amet</td><td>Lorem ipsum dolor sit amet</td><td>Lorem ipsum dolor sit amet</td><td>Lorem ipsum dolor sit amet</td></tr>
      <tr><td>Lorem ipsum dolor sit amet</td><td>Lorem ipsum dolor sit amet</td><td>Lorem ipsum dolor sit amet</td><td>Lorem ipsum dolor sit amet</td></tr>
      <tr><td>Lorem ipsum dolor sit amet</td><td>Lorem ipsum dolor sit amet</td><td>Lorem ipsum dolor sit amet</td><td>Lorem ipsum dolor sit amet</td></tr>
      <tr><td>Lorem ipsum dolor sit amet</td><td>Lorem ipsum dolor sit amet</td><td>Lorem ipsum dolor sit amet</td><td>Lorem ipsum dolor sit amet</td></tr>
      <tr><td>Lorem ipsum dolor sit amet</td><td>Lorem ipsum dolor sit amet</td><td>Lorem ipsum dolor sit amet</td><td>Lorem ipsum dolor sit amet</td></tr>
      <tr><td>Lorem ipsum dolor sit amet</td><td>Lorem ipsum dolor sit amet</td><td>Lorem ipsum dolor sit amet</td><td>Lorem ipsum dolor sit amet</td></tr>
    </tbody>
  </table>
  <div class="foot"><div class="note">Footnote sample: Lorem ipsum dolor sit amet.</div><div class="row"><span>BRACKWELL THORNE EQUITY PARTNERS</span><span>CONFIDENTIAL</span><span>BTEQX.com | 25</span></div></div>
</section>

<!-- 26 Timeline -->
<section class="slide">
  <div class="s-title">Timeline Sample</div><div class="s-sub">Sub Title Goes Here</div><div class="s-rule"></div><div class="mark"></div>
  <div class="abs tiny" style="left:62px;top:78px;width:56px;font-size:3.8px">Lorem ipsum dolor sit amet, consectetur adipiscing elit. Phasellus malesuada vulputate mauris</div>
  <div class="abs tiny" style="left:148px;top:78px;width:56px;font-size:3.8px">Lorem ipsum dolor sit amet, consectetur adipiscing elit. Phasellus malesuada vulputate mauris</div>
  <div class="abs tiny" style="left:234px;top:78px;width:56px;font-size:3.8px">Lorem ipsum dolor sit amet, consectetur adipiscing elit. Phasellus malesuada vulputate mauris</div>
  <svg class="abs" style="left:14px;top:118px" width="310" height="14" viewBox="0 0 310 14" font-family="Archivo,sans-serif" font-weight="800" font-size="4.5" fill="#fff" text-anchor="middle">
    <polygon points="0,2 42,2 48,7 42,12 0,12" fill="var(--blue)"/><text x="22" y="9">JAN</text>
    <polygon points="44,2 86,2 92,7 86,12 44,12 50,7" fill="var(--gold)"/><text x="68" y="9">FEB</text>
    <polygon points="88,2 130,2 136,7 130,12 88,12 94,7" fill="var(--blue)"/><text x="112" y="9">MAR</text>
    <polygon points="132,2 174,2 180,7 174,12 132,12 138,7" fill="var(--gold)"/><text x="156" y="9">APR</text>
    <polygon points="176,2 218,2 224,7 218,12 176,12 182,7" fill="var(--blue)"/><text x="200" y="9">MAY</text>
    <polygon points="220,2 262,2 268,7 262,12 220,12 226,7" fill="var(--gold)"/><text x="244" y="9">JUN</text>
    <polygon points="264,2 304,2 310,7 304,12 264,12 270,7" fill="var(--blue)"/><text x="287" y="9">JUL</text>
  </svg>
  <div class="abs tiny" style="left:18px;top:142px;width:56px;font-size:3.8px">Lorem ipsum dolor sit amet, consectetur adipiscing elit. Phasellus malesuada vulputate mauris</div>
  <div class="abs tiny" style="left:104px;top:142px;width:56px;font-size:3.8px">Lorem ipsum dolor sit amet, consectetur adipiscing elit. Phasellus malesuada vulputate mauris</div>
  <div class="abs tiny" style="left:190px;top:142px;width:56px;font-size:3.8px">Lorem ipsum dolor sit amet, consectetur adipiscing elit. Phasellus malesuada vulputate mauris</div>
  <div class="abs tiny" style="left:262px;top:142px;width:56px;font-size:3.8px">Lorem ipsum dolor sit amet, consectetur adipiscing elit. Phasellus malesuada vulputate mauris</div>
  <div class="foot"><div class="row"><span>BRACKWELL THORNE EQUITY PARTNERS</span><span>CONFIDENTIAL</span><span>BTEQX.com | 26</span></div></div>
</section>

<!-- 27 Meet team -->
<section class="slide">
  <div class="s-title">Meet Our Team</div><div class="s-sub" style="top:29px">Sub Title Goes Here</div><div class="s-rule"></div><div class="mark"></div>
  <div class="photo" role="img" aria-label="Portrait of Martin L. Ashdale" style="left:16px;top:56px;width:72px;height:100px;background:linear-gradient(180deg,#d8dadc,#6d7278)"></div>
  <div class="photo" role="img" aria-label="Portrait of Peter J. Colwyn" style="left:93px;top:56px;width:72px;height:100px;background:linear-gradient(180deg,#d8dadc,#5f6a76)"></div>
  <div class="photo" role="img" aria-label="Portrait of Daniel R. Hewitt" style="left:170px;top:56px;width:72px;height:100px;background:linear-gradient(180deg,#d8dadc,#596474)"></div>
  <div class="photo" role="img" aria-label="Portrait of Graham T. Welford" style="left:247px;top:56px;width:72px;height:100px;background:linear-gradient(180deg,#d8dadc,#525c6b)"></div>
  <div class="abs" style="left:22px;top:162px;font-size:4.6px;line-height:1.3"><b style="color:var(--blue)">Martin L. Ashdale</b><br>Managing Partner</div>
  <div class="abs" style="left:99px;top:162px;font-size:4.6px;line-height:1.3"><b style="color:var(--blue)">Peter J. Colwyn</b><br>Partner</div>
  <div class="abs" style="left:176px;top:162px;font-size:4.6px;line-height:1.3"><b style="color:var(--blue)">Daniel R. Hewitt</b><br>Partner</div>
  <div class="abs" style="left:253px;top:162px;font-size:4.6px;line-height:1.3"><b style="color:var(--blue)">Graham T. Welford</b><br>Managing Director</div>
  <div class="foot"><div class="row"><span>BRACKWELL THORNE EQUITY PARTNERS</span><span>CONFIDENTIAL</span><span>BTEQX.com | 27</span></div></div>
</section>

<!-- 28 Quote with portrait -->
<section class="slide">
  <div class="photo" role="img" aria-label="Portrait of Graham T. Welford" style="left:0;top:0;width:122px;height:218px;background:linear-gradient(180deg,#e2e4e6,#8a9098)"></div>
  <div class="abs" style="left:0;top:218px;width:122px;height:34px;background:var(--navy)"></div>
  <div class="abs" style="left:10px;top:204px;color:#fff;font-family:Archivo,sans-serif;font-weight:800;font-size:9px">Graham T. Welford</div>
  <div class="abs" style="left:10px;top:216px;color:#fff;font-size:4.5px">Managing Director</div>
  <div class="mark"></div>
  <div class="abs" style="left:144px;top:28px;font-family:Archivo,sans-serif;font-weight:900;font-size:30px;color:var(--blue);line-height:1">“</div>
  <div class="abs" style="left:144px;top:66px;width:170px;font-size:5px;font-weight:700;line-height:1.35">Lorem Ipsum has been the industry's standard dummy text ever since the 1500s, <span style="color:var(--blue)">when an unknown</span> printer took a galley of type and scrambled it to make a type specimen book.</div>
  <div class="abs" style="left:144px;top:100px;width:170px;font-size:4.2px;line-height:1.35">Lorem Ipsum is simply dummy text of the printing and typesetting industry. Lorem Ipsum has been the industry's standard dummy text ever since the 1500s, when an unknown printer took a galley of type and scrambled it to make a type specimen book. It has survived not only five centuries, but also the leap into electronic typesetting, remaining essentially unchanged. It was popularised in the 1960s with the release of sheets containing passages, and more recently with desktop publishing software including versions of Lorem Ipsum.</div>
  <div class="foot" style="left:128px"><div class="note">Footnote sample: Lorem ipsum dolor sit amet.</div><div class="row"><span style="width:60px">BRACKWELL THORNE</span><span>CONFIDENTIAL</span><span>BTEQX.com | 28</span></div></div>
</section>

<!-- 29 Quote green -->
<section class="slide">
  <div class="photo" role="img" aria-label="Field engineer in a red hard hat working on site" style="inset:0;clip-path:polygon(70% 0,100% 0,100% 100%,52% 100%);background:linear-gradient(160deg,#9ec4d8,#6b8da0 50%,#3e4d55)"></div>
  <div class="abs" style="inset:0;clip-path:polygon(0 0,70% 0,52% 100%,0 100%);background:linear-gradient(135deg,#5aa683,#3a8f6f 55%,#2f7e6c)"></div>
  <div class="abs" style="left:14px;top:24px;font-family:Archivo,sans-serif;font-weight:900;font-size:34px;color:var(--gold);line-height:1">“</div>
  <div class="abs" style="left:14px;top:64px;width:170px;font-size:6.4px;font-weight:700;line-height:1.35;color:#fff">Lorem Ipsum has been the industry's standard dummy text ever since the 1500s, <span style="color:var(--gold)">when an unknown</span> printer took a galley of type and scrambled it to make a type specimen book.</div>
  <div class="abs" style="left:14px;top:112px;font-size:4.5px;color:#fff">Alex Morrow</div>
  <div class="mark"></div>
  <div class="foot" style="color:#fff"><div class="note" style="color:#dfe">Footnote sample: Lorem ipsum dolor sit amet.</div><div class="row"><span>BRACKWELL THORNE EQUITY PARTNERS</span><span>CONFIDENTIAL</span><span>BTEQX.com | 29</span></div></div>
</section>

<!-- 30 Thank you -->
<section class="slide">
  <div class="photo fill" role="img" aria-label="Team standing together at an industry event" style="background:linear-gradient(150deg,#6b7d8f,#3a3f48 60%,#b24848)"></div>
  <svg class="fill" viewBox="0 0 337 252" aria-hidden="true">
    <defs><linearGradient id="g30" x1="0" y1="0" x2="1" y2="1"><stop offset="0" stop-color="#4fa57f"/><stop offset="1" stop-color="#2f8a86"/></linearGradient></defs>
    <polygon points="0,0 40,0 225,252 0,252" fill="url(#g30)"/>
    <polygon points="40,0 60,0 250,252 225,252" fill="var(--lav)"/>
    <polygon points="337,130 337,252 240,252" fill="var(--lav)"/>
    <polygon points="337,170 337,252 270,252" fill="#fff"/>
  </svg>
  <div class="divtitle abs" style="left:14px;top:68px;font-size:12px">Thank You</div>
  <div class="abs" style="left:14px;top:88px;width:90px;font-size:4.5px;font-weight:700;color:#fff;line-height:1.35">Lorem ipsum dolor sit amet, corpora delicata duo. Rebum insolens pri eu. No alia tota modus qui.</div>
  <div class="abs" style="left:14px;top:160px;font-size:4px;color:#fff;line-height:3">
    <div style="display:flex;align-items:center;gap:4px"><i style="width:6px;height:6px;border-radius:50%;background:var(--gold);display:block"></i>contact@bteqx.com</div>
    <div style="display:flex;align-items:center;gap:4px"><i style="width:6px;height:6px;border-radius:50%;background:var(--gold);display:block"></i>+1 555 0142 880</div>
    <div style="display:flex;align-items:center;gap:4px"><i style="width:6px;height:6px;border-radius:50%;background:var(--gold);display:block"></i>www.bteqx.com</div>
  </div>
  <div class="logo abs" style="left:262px;top:220px;font-size:6px"><i style="width:7px;height:7px"></i><span>BRACKWELL<br>THORNE</span></div>
</section>

</main>
</body>
</html>
```